Branvique needs a business Card Design

We are looking for a business card Design for our new Managed Service Provider Company, Branvique. Branvique encompasses everything IT for the average medium sized business. Our primary services are help desk support, cyber-security (malware and ransomware protection), and Disaster Recovery systems. We would like the design to have a very clean and professional look, with a very minimalist feel.

Target Market(s)

Medium to large sized businesses

Industry/Entity Type

It Service

Contact Information for Business Card

Name GoesHere
name@branvique.com
O: 555-382-6047
C: 555-731-5820

Font styles to use
Other font styles liked:
• Poppins Font Only Please

Colors

Designer to choose only greyscale colors for use in the design.

Requirements
Must have
• Logo included
Nice to have
• Cutting Edge, innovative, minimalistic, elegant

```html
<!DOCTYPE html>
<html lang="en">
<head>
<meta charset="utf-8">
<title>Branvique Business Card</title>
<link href="https://fonts.googleapis.com/css2?family=Poppins:wght@400;500;600&display=swap" rel="stylesheet">
<style>
  :root {
    --charcoal: #262626;
    --ink: #222222;
    --muted: #6b6b6b;
    --card-light: #ffffff;
    --card-shade: #e4e4e4;
    --stage: #4a4a4a;
    --mark-light: #ececec;
  }
  * { margin: 0; padding: 0; box-sizing: border-box; }
  html, body { width: 1200px; height: 900px; overflow: hidden; }
  body {
    background: var(--stage);
    font-family: "Poppins", sans-serif;
    position: relative;
  }
  .card {
    position: absolute;
    left: 340px;
    width: 520px;
    height: 297px;
    border-radius: 16px;
    overflow: hidden;
  }
  .card--front {
    top: 110px;
    background: linear-gradient(135deg, var(--card-shade) 0%, var(--card-light) 45%, var(--card-light) 100%);
    color: var(--ink);
  }
  .card--back {
    top: 483px;
    background: var(--charcoal);
  }
  .wordmark {
    font-weight: 400;
    text-transform: uppercase;
    letter-spacing: 0.42em;
  }
  .card--front .wordmark {
    position: absolute;
    left: 34px;
    top: 28px;
    font-size: 21px;
    color: var(--ink);
  }
  .holder {
    position: absolute;
    left: 34px;
    top: 84px;
  }
  .holder__name {
    font-weight: 600;
    font-size: 20px;
    letter-spacing: 0.02em;
    text-transform: uppercase;
    line-height: 1.1;
  }
  .holder__role {
    font-size: 11px;
    color: var(--muted);
    margin-top: 2px;
  }
  .holder__rule {
    width: 14px;
    height: 1px;
    background: var(--ink);
    margin: 8px 0 7px;
  }
  .holder__address, .contact {
    font-size: 12.5px;
    color: var(--ink);
    line-height: 1.45;
  }
  .contact { margin-top: 4px; list-style: none; }
  .contact li { display: flex; align-items: center; gap: 7px; }
  .contact svg { width: 10px; height: 10px; fill: none; stroke: var(--ink); stroke-width: 1.6; flex-shrink: 0; }
  .front-square {
    position: absolute;
    right: 60px;
    top: 118px;
    width: 110px;
    height: 110px;
    background: var(--charcoal);
  }
  .back-brand {
    position: absolute;
    inset: 0;
    display: flex;
    flex-direction: column;
    align-items: center;
    justify-content: center;
    gap: 22px;
  }
  .back-brand__square {
    width: 46px;
    height: 46px;
    background: var(--mark-light);
  }
  .card--back .wordmark {
    font-size: 28px;
    color: var(--mark-light);
    padding-left: 0.42em;
  }
</style>
</head>
<body>
  <section class="card card--front" aria-label="Business card front">
    <div class="wordmark">Branvique</div>
    <div class="holder">
      <div class="holder__name">Daniel Hart</div>
      <div class="holder__role">Director</div>
      <div class="holder__rule"></div>
      <div class="holder__address">48 Alder Street<br>Fairview, TN 37062</div>
      <ul class="contact">
        <li><svg viewBox="0 0 10 10"><path d="M2 1 L4 3 L3 4.5 Q4.5 6.5 5.5 7 L7 6 L9 8 L7.5 9.3 Q3 8 0.8 2.5 Z"/></svg>555-382-6047</li>
        <li><svg viewBox="0 0 10 10"><rect x="2.5" y="0.8" width="5" height="8.4" rx="1"/><line x1="4.3" y1="7.6" x2="5.7" y2="7.6"/></svg>555-731-5820</li>
        <li><svg viewBox="0 0 10 10"><rect x="0.8" y="2" width="8.4" height="6" rx="0.6"/><path d="M1 2.4 L5 5.4 L9 2.4"/></svg>daniel@branvique.com</li>
        <li><svg viewBox="0 0 10 10"><circle cx="5" cy="5" r="4.2"/><ellipse cx="5" cy="5" rx="1.8" ry="4.2"/><line x1="0.8" y1="5" x2="9.2" y2="5"/></svg>www.branvique.com</li>
      </ul>
    </div>
    <div class="front-square"></div>
  </section>

  <section class="card card--back" aria-label="Business card back">
    <div class="back-brand">
      <div class="back-brand__square"></div>
      <div class="wordmark">Branvique</div>
    </div>
  </section>
</body>
</html>
```